Need help refining Tallbergsgillet

Hi We need help with the refining of overall design and details of our homepage design Tallbergsgillet. See attached files.

Attached files:
homepage.psd - file you can use to work from.
homepage.png – quick notes on thoughts of the design
logo.psd (smart object) – The logo should be in gold.
social media elements.png - what type of data that needs design in the feed

What we need:
Something is missing with the overall design as well as detailed design for our social media feed. We don’t know what and hope you can solve this for us.

The homepage:
Our main page include a selfloading blogfeed combined with Vendraly- and Instagramfeed.

Fonts:
So far I´ve used Roboto regular, and Georgia, but feel free to use other fonts if you find better suited

Among others, we need a better detailed design that works better with the overall design.

Se attached sample image (social_mediafeed.png) what types of data we get from Vendraly in our feed. Feel free to redesign the elements of this data.

Headerlinks:
Even though we only have one page, there should be place for links to other pages as well which will load below the header.

Social media follow: Place for social media follow links/icons/buttons in style with rest of the design. Maybe at top grey border? We use Glimtora and Vendraly in style with rest of the design.

Colors:
The logo should be in gold, and use of "goldish" colors troughout the page.
Also blue elements troughout the page

Logo in gold/goldish color
Blue elements # 13416c (or similar color that works well in the design)

Target Market(s)

Wellness, fitness, spa and food, Exclusive

Number of Pages Required

1 page

Font styles to use
Serif
Sans Serif
Script
Other font styles liked:
• Roboto, Georgia

Requirements
Must have
• Better overall design that feel harmonic.
• Better design of blog and social media feeds (se all attached images)
• Nice clean design, easy on the eye
• Colors on theme: Gold + blue

```html
<!DOCTYPE html>
<html lang="sv">
<head>
<meta charset="utf-8">
<title>Tallbergsgillet</title>
<link href="https://fonts.googleapis.com/css2?family=Federo&family=Roboto:wght@300;400;500;700&family=Playfair+Display:wght@400&display=swap" rel="stylesheet">
<style>
:root{
  --blue:#13416c;
  --blue-dark:#0d2f50;
  --gold:#c9a24a;
  --gold-light:#dcbf7a;
  --ink:#333;
  --muted:#777;
  --line:#dcdcdc;
  --panel:#e6e6e6;
  --white:#fff;
}
*{box-sizing:border-box;margin:0;padding:0}
html,body{width:1200px;height:4018px;overflow:hidden}
body{position:relative;background:var(--white);font-family:"Roboto",Arial,sans-serif;color:var(--ink)}
.abs{position:absolute}

/* Header & hero */
.hero{left:0;top:0;width:1200px;height:718px;background:linear-gradient(180deg,#d9e0d6 0%,#a9b79a 30%,#5f7a4e 55%,#8c9a73 75%,#c8c1ad 100%)}
.header-band{left:0;top:0;width:1200px;height:122px;background:rgba(255,255,255,.86)}
.top-btn{top:16px;height:32px;border:1.5px solid;border-radius:4px;font-size:13px;display:flex;align-items:center;justify-content:center;gap:6px;background:#fff}
.top-btn.member{left:848px;width:112px;color:var(--gold);border-color:var(--gold)}
.top-btn.login{left:970px;width:128px;color:var(--blue);border-color:var(--blue)}
.logo{left:470px;top:18px;width:260px;text-align:center}
.logo-mark{width:30px;height:30px;border-radius:50%;background:var(--gold);margin:0 auto 6px}
.logo-name{font-family:"Federo",serif;font-size:27px;color:var(--gold);letter-spacing:1px}
.main-nav{top:94px;font-size:14px;font-weight:500;color:var(--blue);letter-spacing:.3px}
.nav-rule{top:112px;height:3px;background:var(--blue)}
.dropdown{left:918px;top:122px;width:172px;background:#fff;border:2px solid var(--blue)}
.dropdown li{list-style:none;font-size:11px;padding:0 12px;height:40px;line-height:40px;color:#8a97a6;letter-spacing:.3px}
.dropdown li.active{background:var(--blue);color:var(--gold-light)}
.hero-photo-note{left:0;top:122px;width:1200px;height:596px}
.featured{left:402px;top:262px;width:396px;height:328px;background:rgba(255,255,255,.82);text-align:center;padding:24px 36px}
.featured h1{font-family:"Federo",serif;font-weight:400;font-size:46px;color:var(--blue)}
.featured .title-rule{width:170px;height:2px;background:var(--gold);margin:2px auto 20px}
.featured p{font-size:15px;line-height:21px;color:#444}
.btn{display:inline-flex;align-items:center;justify-content:center;background:var(--blue);color:#fff;font-size:13px;font-weight:500;height:32px;padding:0 22px;border-radius:2px;letter-spacing:.5px}
.featured .btn{margin-top:22px}
.arrow{top:400px;width:46px;height:46px;border-radius:50%;background:rgba(40,40,40,.75);display:flex;align-items:center;justify-content:center}

/* Section headings */
.section-title{left:0;width:1200px;text-align:center;font-family:"Federo",serif;font-size:34px;color:var(--blue)}
.section-title .gold{color:var(--gold)}
.divider{left:540px;width:120px;height:14px}

/* Offer cards */
.offer{top:892px;width:318px;height:408px;border:1px solid #e7e7e7;box-shadow:0 1px 6px rgba(0,0,0,.08);background:#fff}
.offer-img{position:relative;height:246px;background:linear-gradient(180deg,#7b5b93 0%,#c07aa0 40%,#e19a6e 62%,#4b4d7a 100%)}
.offer-img .brand{position:absolute;left:20px;top:18px;font-family:"Federo",serif;font-size:27px;color:#fff}
.offer-img .tag{position:absolute;left:20px;top:80px;font-family:"Federo",serif;font-size:20px;color:#fff}
.badge{position:absolute;left:20px;top:142px;width:74px}
.badge .pct{height:54px;background:var(--gold);color:#fff;font-family:"Federo",serif;font-size:30px;display:flex;align-items:center;justify-content:center}
.badge .lbl{height:26px;background:#fff;color:#333;font-size:14px;display:flex;align-items:center;justify-content:center}
.offer h3{margin:30px 20px 0;font-size:15px;font-weight:700;color:var(--gold);letter-spacing:.5px}
.offer p{margin:10px 20px 0;font-size:15px;color:#333}
.offer .btn{margin:22px 20px 0;height:30px;padding:0 26px}
.rule{left:0;width:1200px;height:1px;background:var(--line)}

/* Blog posts */
.post-title{left:0;width:1200px;text-align:center;font-family:"Federo",serif;font-size:44px;color:#222}
.meta{left:0;width:1200px;text-align:center;font-size:12px;color:#777;letter-spacing:.4px;display:flex;justify-content:center;gap:26px}
.meta span{display:inline-flex;align-items:center;gap:6px}
.meta i{display:inline-block;width:10px;height:10px;border:1.5px solid var(--gold);border-radius:2px}
.post-img{left:102px;width:996px;height:378px;background:linear-gradient(180deg,#f2e2c8 0%,#c8cfd6 38%,#7fa0b6 58%,#c9b391 78%,#8a7f72 100%)}
.excerpt{left:102px;width:996px;font-size:14px;line-height:20px;color:#444}
.share-bar{left:102px;width:996px;height:44px;border-top:1px solid var(--line);border-bottom:1px solid var(--line);display:flex;align-items:center;font-size:12px;color:#777;letter-spacing:.4px}
.share-bar span{display:inline-flex;align-items:center;gap:8px;margin-right:34px}
.share-bar .dot{width:14px;height:14px;border-radius:50%;background:var(--gold)}
.share-bar .btn{margin-left:auto;height:30px;padding:0 26px}

/* Social feed */
.feed{left:102px;top:2144px;width:996px;height:799px;background:var(--panel)}
.feed-card{top:2160px;width:450px;height:766px;background:#fff}
.feed-tag{position:absolute;left:0;top:0;height:20px;padding:0 10px;background:var(--blue);color:#fff;font-size:11px;line-height:20px}
.feed-head{position:absolute;left:24px;top:40px;display:flex;align-items:center;gap:12px;font-size:11px;color:#666}
.avatar{width:36px;height:36px;border-radius:50%;background:var(--blue);border:2px solid var(--gold)}
.feed-head b{color:var(--blue);font-weight:500}
.feed-text{position:absolute;left:24px;top:96px;width:402px;font-size:12px;line-height:17px;color:#444}
.feed-text .tags{color:var(--blue)}
.feed-media{position:absolute;left:24px;top:218px;width:402px;height:460px;border:1px solid var(--line)}
.feed-media .pic{height:356px}
.feed-media h4{font-family:"Playfair Display",Georgia,serif;font-weight:400;font-size:18px;color:#333;margin:20px 20px 0}
.feed-media small{display:block;margin:6px 20px 0;font-size:10px;color:#888;letter-spacing:.5px}
.feed-share{position:absolute;left:0;top:708px;display:flex;align-items:center;gap:6px;font-size:11px;color:#666}
.feed-share .c{width:22px;height:22px;border-radius:50%}

/* Footer */
.footer{left:0;top:3765px;width:1200px;height:228px;background:var(--blue)}
.footer h5{font-size:14px;font-weight:500;color:#fff;letter-spacing:.5px}
.footer p,.footer li{font-size:13px;line-height:20px;color:#b9c6d4;list-style:none}
.follow-grid{display:grid;grid-template-columns:repeat(3,30px);gap:8px;margin-top:18px}
.follow-grid span{width:30px;height:30px;border-radius:50%;border:1.5px solid #b9c6d4}
.news-form{display:flex;margin-top:16px;width:396px;height:36px}
.news-form .input{flex:1;background:#fff;font-size:13px;color:#555;padding:0 12px;display:flex;align-items:center}
.news-form .go{width:90px;background:var(--gold);color:#fff;font-size:13px;font-weight:700;display:flex;align-items:center;justify-content:center}
.copyright{left:0;top:3993px;width:1200px;height:25px;background:var(--blue-dark);color:#fff;font-size:12px;line-height:25px;padding-left:102px}
</style>
</head>
<body>

<header>
  <div class="abs hero" role="img" aria-label="Photo: woman in a yoga stretch on a lakeside pier at sunset"></div>
  <div class="abs header-band"></div>
  <div class="abs top-btn member"><svg width="12" height="12" viewBox="0 0 12 12"><path d="M6 1l1.5 3.2L11 4.6 8.4 7l.7 3.5L6 8.8 2.9 10.5 3.6 7 1 4.6l3.5-.4z" fill="var(--gold)"/></svg>Bli Medlem</div>
  <div class="abs top-btn login"><svg width="12" height="12" viewBox="0 0 12 12"><circle cx="6" cy="4" r="2.5" fill="none" stroke="var(--blue)" stroke-width="1.3"/><path d="M1.5 11.5c0-3 2-4.5 4.5-4.5s4.5 1.5 4.5 4.5" fill="none" stroke="var(--blue)" stroke-width="1.3"/></svg>Medlemslogin</div>
  <div class="abs logo">
    <div class="logo-mark"></div>
    <div class="logo-name">TALLBERGSGILLET</div>
  </div>
  <div class="abs nav-rule" style="left:102px;width:392px"></div>
  <div class="abs nav-rule" style="left:706px;width:392px"></div>
  <nav>
    <span class="abs main-nav" style="left:102px">HEM</span>
    <span class="abs main-nav" style="left:196px">TALLBERGSRESOR</span>
    <span class="abs main-nav" style="left:398px">INSPIRATION</span>
    <span class="abs main-nav" style="left:716px">MEDLEMSERBJUDANDEN</span>
    <span class="abs main-nav" style="left:928px">OM</span>
    <span class="abs main-nav" style="left:1014px">INSPIRATION</span>
  </nav>
  <ul class="abs dropdown">
    <li class="active">TALLBERGSGILLET</li>
    <li>TALLBERGSBILJETTER</li>
    <li>BOKA</li>
  </ul>
  <div class="abs featured">
    <h1>Featured</h1>
    <div class="title-rule"></div>
    <p>Lorem ipsum dolor sit amet, consectetur adipiscing elit, sed do eiusmod tempor incididunt ut labore et dolore magna aliqua. Ut enim ad minim veniam, quis nostrud exercitation ullamco laboris nisi ut aliquip ex ea commodo consequat.</p>
    <span class="btn">LÄS MER</span>
  </div>
  <div class="abs arrow" style="left:14px"><svg width="14" height="18" viewBox="0 0 14 18"><path d="M10 2L3 9l7 7" fill="none" stroke="#fff" stroke-width="3"/></svg></div>
  <div class="abs arrow" style="left:1140px"><svg width="14" height="18" viewBox="0 0 14 18"><path d="M4 2l7 7-7 7" fill="none" stroke="#fff" stroke-width="3"/></svg></div>
</header>

<main>
  <h2 class="abs section-title" style="top:788px">TALLBERGSGILLETS <span class="gold">MEDLEMSERBJUDANDEN</span></h2>
  <svg class="abs divider" style="top:842px" viewBox="0 0 120 14"><line x1="0" y1="7" x2="50" y2="7" stroke="var(--gold)"/><circle cx="60" cy="7" r="4" fill="var(--gold)"/><line x1="70" y1="7" x2="120" y2="7" stroke="var(--gold)"/></svg>

  <article class="abs offer" style="left:102px">
    <div class="offer-img" role="img" aria-label="Photo: coastal town at dusk under a purple sky">
      <span class="brand">Hälsa &amp; skönhet AB</span><span class="tag">Motionera Mera</span>
      <div class="badge"><div class="pct">30%</div><div class="lbl">Rabatt!</div></div>
    </div>
    <h3>HÄLSA &amp; SKÖNHET AB</h3><p>En kort rubrik på erbjudandet</p><span class="btn">LÄS MER</span>
  </article>
  <article class="abs offer" style="left:441px">
    <div class="offer-img" role="img" aria-label="Photo: coastal town at dusk under a purple sky">
      <span class="brand">Hälsa &amp; skönhet AB</span><span class="tag">Motionera Mera</span>
      <div class="badge"><div class="pct">30%</div><div class="lbl">Rabatt!</div></div>
    </div>
    <h3>HÄLSA &amp; SKÖNHET AB</h3><p>En kort rubrik på erbjudandet</p><span class="btn">LÄS MER</span>
  </article>
  <article class="abs offer" style="left:780px">
    <div class="offer-img" role="img" aria-label="Photo: coastal town at dusk under a purple sky">
      <span class="brand">Hälsa &amp; skönhet AB</span><span class="tag">Motionera Mera</span>
      <div class="badge"><div class="pct">30%</div><div class="lbl">Rabatt!</div></div>
    </div>
    <h3>HÄLSA &amp; SKÖNHET AB</h3><p>En kort rubrik på erbjudandet</p><span class="btn">LÄS MER</span>
  </article>

  <div class="abs rule" style="top:1340px"></div>

  <!-- Blog post 1 -->
  <h2 class="abs post-title" style="top:1388px">En trevlig rubrik på ditt blogginlägg</h2>
  <svg class="abs divider" style="top:1454px" viewBox="0 0 120 14"><line x1="0" y1="7" x2="50" y2="7" stroke="var(--gold)"/><circle cx="60" cy="7" r="4" fill="var(--gold)"/><line x1="70" y1="7" x2="120" y2="7" stroke="var(--gold)"/></svg>
  <div class="abs meta" style="top:1494px"><span><i></i>22 OKTOBER, 2016</span><span><i></i>AV TALLBERGSGILLET</span><span><i></i>0 KOMMENTARER</span><span><i></i>SPA, LIVSNJUTNING, YOGA</span></div>
  <div class="abs post-img" style="top:1538px" role="img" aria-label="Photo: woman meditating on a pier by the sea at sunrise"></div>
  <p class="abs excerpt" style="top:1952px">ed dui consectetur, eleifend nibh et, ultricies justo. Vivamus luctus elit ac lacus placerat laoreet vel at lacus. Sed a molestie ex. Vestibulum ac varius libero. Fusce sollicitudin non tellus lacinia molestie. Sed rhoncus dui a sem accumsan, nec scelerisque augue suscipit. Aliquam eget justo odio. Maecenas in molestie tortor, eu tristique ligula. Suspendisse vulputate urna ut elit iacul varius.</p>
  <div class="abs share-bar" style="top:2042px"><span><i class="dot"></i>DELA</span><span><i class="dot"></i>KOMMENTERA</span><span class="btn">LÄS MER</span></div>

  <!-- Social feed -->
  <section class="abs feed"></section>
  <article class="abs feed-card" style="left:118px">
    <span class="feed-tag">Vendraly</span>
    <div class="feed-head"><span class="avatar"></span><b>Tallbergsgillet</b><span>23 oktober 19:21</span><span>♡ 3</span><span>1 kommentare</span></div>
    <p class="feed-text">Boosta din fräscha!<br>Skiva ingefära och citron och häll hett vatten över. Detta är en fantastisk dryck att börja dagen med. Citronen säger hej till kroppen och ingefäran ger en härlig värme. Denna välgörande dryck är full av antioxidanter som stärker kroppen och ger massor av energi. En god morgonrutin för en toppendag.</p>
    <div class="feed-media">
      <div class="pic" role="img" aria-label="Photo: two glasses of lemon water on a jetty by the sea" style="background:linear-gradient(180deg,#cfdbe6 0%,#8fa7bd 45%,#c7b48a 70%,#6e6454 100%)"></div>
      <h4>Timeline Photos</h4><small>VENDRALY.COM</small>
    </div>
    <div class="feed-share"><span>Dela på</span><i class="c" style="background:#2f5597"></i><i class="c" style="background:#c8463a"></i><i class="c" style="background:#1f6fa8"></i><i class="c" style="background:#3aa0d8"></i></div>
  </article>
  <article class="abs feed-card" style="left:633px">
    <span class="feed-tag">Glimtora</span>
    <div class="feed-head"><span class="avatar"></span><b>Tallbergsgillet</b><span>28 oktober 19:24</span><span>♡ 5</span><span>1 kommentar</span></div>
    <p class="feed-text">Nu är det dags att njuta av lugnet i ett av våra nya hotellrum, redo för en avkopplande helg. Den kändan ...<br><span class="tags">#långhelg #vilmånande #momentsofhappiness #livsnjutare #tallbergsgillet</span></p>
    <div class="feed-media">
      <div class="pic" role="img" aria-label="Photo: hotel room with a made double bed and warm lamps" style="background:linear-gradient(180deg,#cbb59a 0%,#a98b6c 40%,#e9e4dc 62%,#6b3c44 100%)"></div>
      <h4>Timeline Photos</h4><small>GLIMTORA.COM</small>
    </div>
    <div class="feed-share"><span>Dela på</span><i class="c" style="background:#2f5597"></i><i class="c" style="background:#c8463a"></i><i class="c" style="background:#1f6fa8"></i><i class="c" style="background:#3aa0d8"></i></div>
  </article>

  <!-- Blog post 2 -->
  <h2 class="abs post-title" style="top:2985px">En trevlig rubrik på ditt blogginlägg</h2>
  <svg class="abs divider" style="top:3052px" viewBox="0 0 120 14"><line x1="0" y1="7" x2="50" y2="7" stroke="var(--gold)"/><circle cx="60" cy="7" r="4" fill="var(--gold)"/><line x1="70" y1="7" x2="120" y2="7" stroke="var(--gold)"/></svg>
  <div class="abs meta" style="top:3092px"><span><i></i>22 OKTOBER, 2016</span><span><i></i>AV TALLBERGSGILLET</span><span><i></i>0 KOMMENTARER</span><span><i></i>SPA, LIVSNJUTNING, YOGA</span></div>
  <div class="abs post-img" style="top:3135px" role="img" aria-label="Photo: woman meditating on a pier by the sea at sunrise"></div>
  <p class="abs excerpt" style="top:3550px">ed dui consectetur, eleifend nibh et, ultricies justo. Vivamus luctus elit ac lacus placerat laoreet vel at lacus. Sed a molestie ex. Vestibulum ac varius libero. Fusce sollicitudin non tellus lacinia molestie. Sed rhoncus dui a sem accumsan, nec scelerisque augue suscipit. Aliquam eget justo odio. Maecenas in molestie tortor, eu tristique ligula. Suspendisse vulputate urna ut elit iacul varius.</p>
  <div class="abs share-bar" style="top:3638px"><span><i class="dot"></i>DELA</span><span><i class="dot"></i>KOMMENTERA</span><span class="btn">LÄS MER</span></div>
</main>

<footer>
  <div class="abs footer"></div>
  <div class="abs" style="left:102px;top:3790px;width:220px">
    <h5>ABOUT US</h5>
    <p style="margin-top:14px">Lorem ipsum dolor sit amet, consectetur adipiscing elit, sed do eiusmod tempor incididunt ut labore et dolore magna aliqua. Ut enim ad minim veniam, quis nostrud exercitation ullamco laboris nisi ut aliquip ex ea commodo consequat.</p>
  </div>
  <div class="abs" style="left:356px;top:3790px">
    <h5>QUICK LINKS</h5>
    <ul style="margin-top:14px"><li>Hem</li><li>Tallbergsresor</li><li>Inspiration</li><li>Medlemserbjudanden</li><li>Om</li><li>Inspiration</li></ul>
  </div>
  <div class="abs" style="left:528px;top:3790px">
    <h5>FOLLOW US</h5>
    <div class="follow-grid"><span></span><span></span><span></span><span></span><span></span><span></span></div>
  </div>
  <div class="abs" style="left:702px;top:3790px;width:396px">
    <h5>NEWSLETTER SIGN UP</h5>
    <p style="margin-top:14px">Lorem ipsum dolor sit amet, consectetur adipiscing elit, sed do eiusmod tempor incididunt ut labore et dolore et.</p>
    <div class="news-form"><span class="input">Enter your email adress</span><span class="go">SIGN UP</span></div>
  </div>
  <div class="abs copyright">© 2016 Tallbergsgillet. All Rights Reserved</div>
</footer>

</body>
</html>
```